Business Card for Marriage Commissioner

I am a marriage commissioner in the province of Alberta, meaning that I perform civil unions here. I have been trying to think of a unique design for my business card, something a bit different. A lot of "unique" designs seem to incorporate unique cuts or "some assembly required" or printed on plastic or meat. I would like my design to be a full colour card that is a typical business card size.

The information on the card should have:
Lou Varnik
my occupation: Marriage Commissioner
my website: www.louvarnik.ca
my e-mail: lou@louvarnik.ca
my phone: 780-418-2964

I originally submitted a design to the printer that had a screen capture of a findly search window, with my name and occupation in the text box. And underneath that, my phone number. Nothing else. They indicated they could not print this because it was a copyright violation.

One option on the design is I am a retired chemist-so a chemistry themed card would also be of interest, as long as it isn't a "Rusted Tide" theme, as I have that on my other business cards already...

I would prefer a single sided card, but I am open to a double sided card if it is clever!

I would also prefer not to have pictures of male and female couples as in my position I will also marry same sex couples. Same thing for male/female symbols. Someone has submitted two graduated cylinders in love, which is very clever, and gets around this male/female type.

Thanks for your help and interest.

Target Market(s)

Young couples.

Industry/Entity Type

Plastic

Requirements
Nice to have
• chemistry ideas!
Should not have
• Male/female pictures, male/female symbols.
No QR codes.
No transparent designs, will go on paper stock.

```html
<!DOCTYPE html>
<html lang="en">
<head>
<meta charset="utf-8">
<title>Lou Varnik – Marriage Commissioner</title>
<link href="https://fonts.googleapis.com/css2?family=Pinyon+Script&family=EB+Garamond:ital@0;1&display=swap" rel="stylesheet">
<style>
  :root {
    --backdrop: #2b2b2b;
    --card: #1b1b1b;
    --card-edge: #262626;
    --ink: #ecebe6;
    --ink-soft: #d4d3cd;
    --bouquet-a: #f3ece2;
    --bouquet-b: #c9a3a0;
    --rings-a: #f4f3f1;
    --rings-b: #cfcac3;
    --couple-a: #e9e6df;
    --couple-b: #6f6a5f;
  }
  * { margin: 0; padding: 0; box-sizing: border-box; }
  html, body {
    width: 1200px; height: 1000px; overflow: hidden;
    background: var(--backdrop);
  }
  .canvas {
    width: 1200px; height: 1000px;
    display: flex; align-items: center; justify-content: center;
  }
  .business-card {
    position: relative;
    width: 1000px; height: 572px;
    background: var(--card);
    border: 1px solid var(--card-edge);
    border-radius: 26px;
    box-shadow: 0 18px 40px rgba(0,0,0,.45);
  }
  .identity {
    position: absolute; left: 150px; top: 52px;
    width: 420px; text-align: center;
    color: var(--ink);
  }
  .identity__name {
    font-family: "Pinyon Script", cursive;
    font-weight: 400;
    font-size: 96px; line-height: 1;
  }
  .identity__role {
    font-family: "EB Garamond", serif;
    font-size: 28px; letter-spacing: 3px;
    margin-top: 6px;
  }
  .gallery {
    position: absolute; left: 70px; top: 215px;
    display: flex; gap: 22px;
  }
  .gallery__photo { width: 270px; height: 195px; display: block; }
  .gallery__photo--bouquet { background: linear-gradient(135deg, var(--bouquet-a) 35%, var(--bouquet-b) 70%, #4e6a44); }
  .gallery__photo--rings { background: radial-gradient(circle at 60% 65%, #d6a86a 0 12%, transparent 13%), linear-gradient(160deg, var(--rings-a), var(--rings-b)); }
  .gallery__photo--couple { background: linear-gradient(90deg, var(--couple-b) 0 35%, var(--couple-a) 55%, #c8c9a6); }
  .contact {
    position: absolute; left: 330px; top: 432px;
    font-family: "EB Garamond", serif;
    font-size: 30px; line-height: 1.22;
    letter-spacing: 1.5px;
    color: var(--ink-soft);
    list-style: none;
  }
  .contact__value { font-style: italic; }
</style>
</head>
<body>
<main class="canvas">
  <article class="business-card">
    <header class="identity">
      <h1 class="identity__name">Lou Varnik</h1>
      <p class="identity__role">Marriage Commissioner</p>
    </header>
    <section class="gallery">
      <span class="gallery__photo gallery__photo--bouquet" role="img" aria-label="Photo of a pink and white rose wedding bouquet on a table"></span>
      <span class="gallery__photo gallery__photo--rings" role="img" aria-label="Photo of two gold wedding rings on white satin"></span>
      <span class="gallery__photo gallery__photo--couple" role="img" aria-label="Photo of a wedding couple holding a bouquet"></span>
    </section>
    <ul class="contact">
      <li>Phone: <span class="contact__value">780-418-2964</span></li>
      <li>Email: <span class="contact__value">lou@louvarnik.ca</span></li>
      <li>Website: <span class="contact__value">www.louvarnik.ca</span></li>
    </ul>
  </article>
</main>
</body>
</html>
```